Crestfield Slab & Tile Needs a Business Card

Attached you will find your logo, my photo and design guidelines for a new business card. The final design will need two separate files to create an embossed card. The cards will be printed by www.plimbo.com (Instructions below)
Format is the Plimbo SQUARE card
Crestfield Slab And Tile is a brick and mortar, retail stone and tile shop.
One the front:
Crestfield Slab And Tile
Gerald Pennock
Owner
48207 Dunmore Ridge Blvd
Suite R & T
Charlotte, NC 28226
Cell: 704-555-0183
Web: www.CrestfieldSlabAndTile.com
(Make each word of the domain a different or alternating color)
On the back;
Something that shows beautiful colorful tile
Follow the design guide closely please. For more information see this page that describes creating the spot gloss file: https://www.plimbo.com/us/business-cards/design-guidelines-spot-gloss
The logo is what we would like to have raised spot glossed.
Contact Information for Business Card
Format is the Plimbo SQUARE card. See attahced guidlines.

```html
<!DOCTYPE html>
<html lang="en">
<head>
<meta charset="utf-8">
<title>Crestfield Slab &amp; Tile — Business Card</title>
<link rel="stylesheet" href="https://fonts.googleapis.com/css2?family=Lato:wght@400;700&display=swap">
<style>
  :root {
    --stage: #d3d4d6;
    --card: #ffffff;
    --ink: #1f2d3a;
    --text: #2e3338;
    --accent: #b5482a;
    --gold: #c58a3a;
    --tile-blue: #1d2f8f;
    --tile-gold: #f2b120;
    --tile-orange: #e8611c;
    --tile-green: #1f7a5a;
    --tile-cream: #f1ece0;
  }
  * { margin: 0; padding: 0; box-sizing: border-box; }
  html, body { width: 1200px; height: 706px; overflow: hidden; }
  body {
    background: var(--stage);
    font-family: "Lato", sans-serif;
    position: relative;
  }
  .card {
    position: absolute;
    width: 485px;
    height: 485px;
    border-radius: 30px;
    box-shadow: 0 4px 14px rgba(0,0,0,0.18);
    overflow: hidden;
  }
  .card--front { left: 85px; top: 95px; background: var(--card); }
  .card--back { left: 608px; top: 88px; }

  .brand {
    position: absolute;
    left: 0; right: 0; top: 14px;
    height: 106px;
    display: flex;
    align-items: center;
    justify-content: center;
    gap: 18px;
    color: var(--ink);
    font-weight: 400;
  }
  .brand__mark {
    width: 96px; height: 96px;
    background: var(--accent);
    flex: none;
  }
  .brand__name { text-align: center; line-height: 1; }
  .brand__primary {
    display: block;
    font-size: 36px;
    letter-spacing: 4px;
    margin-right: -4px;
    text-transform: uppercase;
    padding-bottom: 9px;
    border-bottom: 1px solid var(--gold);
  }
  .brand__secondary {
    display: block;
    font-size: 15px;
    letter-spacing: 12px;
    text-transform: uppercase;
    padding-top: 11px;
    margin-right: -12px;
  }

  .portrait {
    position: absolute;
    left: 160px; top: 124px;
    width: 163px; height: 163px;
    background: linear-gradient(160deg, #3a3c40 0%, #2a2b2e 55%, #4a3f3a 100%);
  }

  .person {
    position: absolute;
    left: 0; right: 0; top: 300px;
    text-align: center;
    color: var(--ink);
  }
  .person__name { font-size: 24px; font-weight: 700; letter-spacing: -0.2px; line-height: 1.2; }
  .person__role { font-size: 16px; color: var(--text); margin-top: 4px; }

  .contact {
    position: absolute;
    left: 0; right: 0;
    display: flex;
    align-items: center;
    justify-content: center;
    gap: 12px;
    font-size: 16px;
    color: var(--text);
  }
  .contact--phone { top: 364px; }
  .contact--web { top: 398px; }
  .contact__icon { width: 18px; height: 18px; fill: var(--accent); }
  .domain__alt { color: var(--accent); }

  .address {
    position: absolute;
    left: 0; right: 0; top: 426px;
    text-align: center;
    font-size: 16px;
    line-height: 20px;
    color: var(--text);
  }

  .tile-art {
    width: 100%; height: 100%;
    background: radial-gradient(circle at 50% 50%,
      var(--tile-gold) 0%,
      var(--tile-orange) 16%,
      var(--tile-cream) 36%,
      var(--tile-green) 52%,
      var(--tile-gold) 62%,
      var(--tile-blue) 78%);
  }
</style>
</head>
<body>
  <section class="card card--front">
    <div class="brand">
      <div class="brand__mark"></div>
      <div class="brand__name">
        <span class="brand__primary">Crestfield</span>
        <span class="brand__secondary">Slab &amp; Tile</span>
      </div>
    </div>

    <div class="portrait" role="img" aria-label="Portrait photo of Gerald Pennock, owner"></div>

    <div class="person">
      <div class="person__name">Gerald Pennock</div>
      <div class="person__role">Owner</div>
    </div>

    <div class="contact contact--phone">
      <svg class="contact__icon" viewBox="0 0 24 24" aria-hidden="true">
        <path d="M6.6 10.8c1.4 2.8 3.8 5.1 6.6 6.6l2.2-2.2c.3-.3.7-.4 1-.2 1.1.4 2.3.6 3.6.6.6 0 1 .4 1 1V20c0 .6-.4 1-1 1C10.6 21 3 13.4 3 4c0-.6.4-1 1-1h3.5c.6 0 1 .4 1 1 0 1.3.2 2.5.6 3.6.1.3 0 .7-.2 1l-2.3 2.2z"/>
      </svg>
      <span>704-555-0183</span>
    </div>

    <div class="contact contact--web">
      <svg class="contact__icon" viewBox="0 0 24 24" aria-hidden="true">
        <path d="M2 5h20v14H2z M3.5 6.5 12 12.5l8.5-6z" fill-rule="evenodd"/>
      </svg>
      <span class="domain">www.<span class="domain__alt">Crestfield</span>Slab<span class="domain__alt">And</span>Tile.com</span>
    </div>

    <div class="address">
      48207 Dunmore Ridge Blvd<br>
      Suite R &amp; T Charlotte, NC 28226
    </div>
  </section>

  <section class="card card--back">
    <div class="tile-art" role="img" aria-label="Colorful glazed ceramic tile with a blue, gold, orange, green and cream floral medallion"></div>
  </section>
</body>
</html>
```